Webdesign für Honigmanufaktur
Zielgruppe
Imkerei, Verkauf von Honig und Honigerzeugnissen, so wie Bienenwachskerzen.
Zielgruppe sind vermutlich Frauen im mittleren bis gehobenen Alter.
Aufgabenstellung
Es gibt ein Firmenlogo.
Ich bevorzuge als Grundfarbe weiß, lasse mich aber von guten Einfällen gerne überraschen.
Die Website www.velunda.at finde ich sehr ansprechend.
Nur ohne Musik.
Ohne Deutsch/Englisch Auswahl.
Es soll danach Word press verwendet werden.

```html
<!DOCTYPE html>
<html lang="de">
<head>
<meta charset="utf-8">
<title>Imkerei Lindenhain – Mobile Webdesign</title>
<link href="https://fonts.googleapis.com/css2?family=Oswald:wght@400;500&family=Noto+Serif:wght@400;500&display=swap" rel="stylesheet">
<style>
:root{
  --honey:#e8952c;
  --honey-dark:#c9731a;
  --ink:#333;
  --muted:#777;
  --line:#e2e2e2;
  --frame:#d6d6d6;
  --stage:#f0f0f0;
  --field:#f1f1f1;
  --shade:#9a9a9a;
}
*{box-sizing:border-box;margin:0;padding:0}
html,body{width:1200px;height:2371px;overflow:hidden;background:#fff}
body{position:relative;font-family:"Noto Serif",Georgia,serif;color:var(--ink)}
.stage{position:absolute;left:0;top:0;width:1200px;height:761px;background:var(--stage)}
.screen{position:absolute;background:#fff;border:1px solid var(--frame);display:flex;flex-direction:column;overflow:hidden;box-shadow:0 2px 6px rgba(0,0,0,.08)}
.status{height:13px;flex:none;border-bottom:1px solid var(--line);font:6px/12px Arial,sans-serif;color:#555;text-align:center;background:#fafafa}
.status.dark{background:#111;color:#ddd;text-align:right;padding-right:10px;border:none}
.topbar{height:40px;flex:none;position:relative;border-bottom:1px solid var(--line)}
.burger{position:absolute;left:10px;top:14px;width:15px;height:11px;border-top:2px solid #222;border-bottom:2px solid #222}
.burger::after{content:"";position:absolute;left:0;right:0;top:2.5px;border-top:2px solid #222}
.brand{position:absolute;left:50%;top:6px;transform:translateX(-50%);display:flex;flex-direction:column;align-items:center;gap:2px}
.brand-dot{width:14px;height:14px;border:2.5px solid var(--honey);border-radius:50%}
.brand-name{font:500 5px/1 Oswald,sans-serif;color:var(--honey);letter-spacing:.5px}
.content{padding:10px 10px 0;flex:1;display:flex;flex-direction:column}
.photo{height:114px;flex:none}
.photo.lavender{background:linear-gradient(180deg,#4f6a3b,#8aa25f 45%,#3e5a2c)}
.photo.bees{background:linear-gradient(160deg,#e9e6e0,#b98a4f 60%,#6b4b28)}
.photo.jar{background:linear-gradient(120deg,#9a7aa0,#e9e4de 45%,#e79a2a 75%,#f3efe9)}
.photo.comb{background:linear-gradient(150deg,#d08a1e,#f2b43a 50%,#b8721a)}
.photo.jars{background:linear-gradient(90deg,#eeeeee,#e59b2b 30%,#efefef 50%,#e59b2b 70%,#efefef)}
.photo.candles{background:linear-gradient(160deg,#f3d27a,#e9b548 50%,#b9a58a)}
.photo.flower{background:linear-gradient(180deg,#8b8fc0,#4f7a33 55%,#2f5220)}
h2{font:400 10px/1 Oswald,sans-serif;color:var(--honey);letter-spacing:1.2px;text-transform:uppercase;margin:14px 2px 9px}
.copy{font-size:7.2px;line-height:12.6px;text-align:justify;padding:0 2px;letter-spacing:.2px}
.illus{flex:1;display:flex;align-items:center;justify-content:center;min-height:90px}
.illus span{display:block;width:100px;height:100px;border-radius:50%;background:radial-gradient(circle,#f5b63a,#e8952c 50%,rgba(255,255,255,0) 72%)}
.illus.bee span{background:radial-gradient(circle,#555,#a88a5a 40%,rgba(255,255,255,0) 70%)}
.btn{align-self:flex-start;margin:12px 2px 0;border:1.5px solid var(--honey);font:500 7px/1 "Noto Serif",serif;letter-spacing:1.5px;padding:7px 12px;color:var(--ink)}
.footer{flex:none;border-top:1px solid var(--line);margin-top:auto;padding:7px 8px;font-size:5.6px;line-height:10px;text-align:center;color:#555}
.footer u{text-decoration:underline}
.menu{display:flex;flex-direction:row}
.menu-panel{flex:1;display:flex;flex-direction:column}
.menu-icons{height:50px;display:flex;justify-content:space-around;align-items:center;border-bottom:1px solid var(--line)}
.menu-icons svg{width:16px;height:16px;fill:none;stroke:#333;stroke-width:1.3}
.menu-list{list-style:none}
.menu-list li{font-size:8.5px;letter-spacing:2px;padding:10px 9px 9px;border-bottom:1px solid var(--line);text-transform:uppercase}
.menu-shade{width:40px;background:var(--shade);position:relative;flex:none}
.menu-shade .close{position:absolute;left:0;top:0;width:40px;height:50px;display:flex;align-items:center;justify-content:center}
.menu-shade .peek{position:absolute;left:0;top:50px;width:30px;height:114px;background:linear-gradient(180deg,#4f6a3b,#8aa25f 45%,#3e5a2c);opacity:.7}
.form{display:flex;flex-direction:column;gap:9px;margin-top:2px}
.field{background:var(--field);border:1px solid var(--line);height:22px;font-size:7px;letter-spacing:1.5px;padding:7px 8px;color:#555}
.field.area{height:92px}
.biglogo{display:flex;flex-direction:column;align-items:center;margin-top:26px;gap:8px}
.biglogo .mark{width:56px;height:56px;border-radius:50%;border:6px solid var(--honey)}
.biglogo .name{font:500 15px/1 Oswald,sans-serif;color:var(--honey);letter-spacing:1.5px;text-align:center}
.contact{text-align:center;font-size:7.6px;line-height:13px;margin-top:10px}
.contact .web{color:var(--honey)}
.social{width:32px;height:32px;border-radius:50%;background:#3b5ea8;margin:10px auto 16px}
</style>
</head>
<body>

<div class="stage"></div>

<!-- Stage: menu -->
<div class="screen menu-screen" style="left:183px;top:190px;width:214px;height:382px">
  <div class="status dark">100 %</div>
  <div class="menu" style="flex:1">
    <div class="menu-panel">
      <div class="menu-icons">
        <svg viewBox="0 0 16 16"><path d="M2 8 8 2.5 14 8M4 7v7h8V7"/></svg>
        <svg viewBox="0 0 16 16"><circle cx="8" cy="5.5" r="3"/><path d="M2.5 14.5c0-3 2.5-5 5.5-5s5.5 2 5.5 5z"/></svg>
        <svg viewBox="0 0 16 16"><circle cx="7" cy="7" r="4.5"/><path d="M10.3 10.3 14 14"/></svg>
      </div>
      <ul class="menu-list">
        <li>Die Manufaktur</li><li>Der Honig</li><li>Das Bienenwachs</li><li>Shop</li><li>Kontakt</li><li>Impressum</li><li>Disclaimer</li>
      </ul>
    </div>
    <div class="menu-shade"><div class="close"><svg width="12" height="12" viewBox="0 0 12 12" stroke="#fff" stroke-width="1.4"><path d="M1 1l10 10M11 1 1 11"/></svg></div><div class="peek" role="img" aria-label="Foto Lavendel mit Biene"></div></div>
  </div>
</div>

<!-- Stage: home -->
<div class="screen" style="left:496px;top:190px;width:214px;height:382px">
  <div class="status dark">100 %</div>
  <div class="topbar"><div class="burger"></div><div class="brand"><span class="brand-dot"></span><span class="brand-name">LINDENHAIN</span></div></div>
  <div class="content">
    <div class="photo lavender" role="img" aria-label="Foto Lavendelfeld mit Biene"></div>
    <h2>Die Imkerei Lindenhain</h2>
    <p class="copy">Die Imkerei Lindenhain ist eine kleine, feine Bio-Honig-Manufaktur mit dem großen Ehrgeiz, Ihnen den feinsten und besten Honig zu liefern, den Sie je gekostet haben. Lorem ipsum dolor sit amet, consetetur sadipscing elitr, sed diam nonumy eirmod tempor invidunt ut labore et dolore magna aliquyam erat, sed diam voluptua sadipscing elitr, sedde diam nonumy eirmod tempored invidunt ut labore et dolore magna aliquyam erat.</p>
  </div>
</div>

<!-- Stage: home scrolled -->
<div class="screen" style="left:809px;top:190px;width:214px;height:382px">
  <div class="status dark">100 %</div>
  <div class="content">
    <h2 style="margin-top:14px">Die Imkerei Lindenhain</h2>
    <p class="copy">Die Imkerei Lindenhain ist eine kleine, feine Bio-Honig-Manufaktur mit dem großen Ehrgeiz, Ihnen den feinsten und besten Honig zu liefern, den Sie je gekostet haben. Lorem ipsum dolor sit amet, consetetur sadipscing elitr, sed diam nonumy eirmod tempor invidunt ut labore et dolore magna aliquyam erat, sed diam voluptua sadipscing elitr, sedde diam nonumy eirmod tempored invidunt ut labore et dolore magna aliquyam erat.</p>
    <div class="illus" role="img" aria-label="Illustration Honiglöffel mit fließendem Honig"><span></span></div>
  </div>
  <div class="footer">Copyright © 2018 Imkerei Lindenhain | Musterstraße 10 | 12345 Musterstadt | Tel. 012 345 678 | info@lindenhain-imkerei.de | <u>Disclaimer</u> | <u>Impressum</u></div>
</div>

<!-- Grid: menu -->
<div class="screen" style="left:63px;top:823px;width:233px;height:425px">
  <div class="status">iPhone 6/7/8</div>
  <div class="menu" style="flex:1">
    <div class="menu-panel">
      <div class="menu-icons">
        <svg viewBox="0 0 16 16"><path d="M2 8 8 2.5 14 8M4 7v7h8V7"/></svg>
        <svg viewBox="0 0 16 16"><circle cx="8" cy="5.5" r="3"/><path d="M2.5 14.5c0-3 2.5-5 5.5-5s5.5 2 5.5 5z"/></svg>
        <svg viewBox="0 0 16 16"><circle cx="7" cy="7" r="4.5"/><path d="M10.3 10.3 14 14"/></svg>
      </div>
      <ul class="menu-list">
        <li>Die Manufaktur</li><li>Der Honig</li><li>Das Bienenwachs</li><li>Shop</li><li>Kontakt</li><li>Impressum</li><li>Disclaimer</li>
      </ul>
    </div>
    <div class="menu-shade"><div class="close"><svg width="12" height="12" viewBox="0 0 12 12" stroke="#fff" stroke-width="1.4"><path d="M1 1l10 10M11 1 1 11"/></svg></div><div class="peek" role="img" aria-label="Foto Lavendel mit Biene"></div></div>
  </div>
</div>

<!-- Grid: Manufaktur -->
<div class="screen" style="left:345px;top:823px;width:231px;height:558px">
  <div class="status">iPhone 6/7/8</div>
  <div class="topbar"><div class="burger"></div><div class="brand"><span class="brand-dot"></span><span class="brand-name">LINDENHAIN</span></div></div>
  <div class="content">
    <div class="photo lavender" role="img" aria-label="Foto Lavendelfeld mit Biene"></div>
    <h2>Die Imkerei Lindenhain</h2>
    <p class="copy">Die Imkerei Lindenhain ist eine kleine, feine Bio-Honig-Manufaktur mit dem großen Ehrgeiz, Ihnen den feinsten und besten Honig zu liefern, den Sie je gekostet haben. Lorem ipsum dolor sit amet, consetetur sadipscing elitr, sed diam nonumy eirmod tempor invidunt ut labore et dolore magna aliquyam erat, sed diam voluptua sadipscing elitr, sedde diam nonumy eirmod tempored invidunt ut labore et dolore magna aliquyam erat, sed diam voluptua.</p>
    <div class="illus" role="img" aria-label="Illustration Honiglöffel mit fließendem Honig"><span></span></div>
  </div>
  <div class="footer">Copyright © 2018 Imkerei Lindenhain | Musterstraße 10 | 12345 Musterstadt | Tel. 012 345 678 | info@lindenhain-imkerei.de | <u>Disclaimer</u> | <u>Impressum</u></div>
</div>

<!-- Grid: Team -->
<div class="screen" style="left:627px;top:823px;width:231px;height:558px">
  <div class="status">iPhone 6/7/8</div>
  <div class="topbar"><div class="burger"></div><div class="brand"><span class="brand-dot"></span><span class="brand-name">LINDENHAIN</span></div></div>
  <div class="content">
    <div class="photo bees" role="img" aria-label="Foto Bienen am Flugloch des Bienenstocks"></div>
    <h2>Das Team der Imkerei</h2>
    <p class="copy">Lorem ipsum dolor ma sitted amet, consetetur sadipscing elitr, sed diam nonumy eirmod tempor invidunt ut labore et dolore magdena aliquyam erat, sed diam voluptua. At vero eos et accusam et justo duo dolores et ea rebum. Stet clita kasd gubergren, no sea takimata sanctus est Lorem ipsum dolor sit amet. Lorem ipsum dolor sit amet, consetetur sadipscing elitr, sedde diam nonumy eirmod tempored invidunt ut labore et dolore magna aliquyam erat, sed diam voluptua.</p>
    <div class="illus bee" role="img" aria-label="Illustration fliegende Hummel"><span></span></div>
  </div>
  <div class="footer">Copyright © 2018 Imkerei Lindenhain | Musterstraße 10 | 12345 Musterstadt | Tel. 012 345 678 | info@lindenhain-imkerei.de | <u>Disclaimer</u> | <u>Impressum</u></div>
</div>

<!-- Grid: Honig -->
<div class="screen" style="left:907px;top:823px;width:231px;height:558px">
  <div class="status">iPhone 6/7/8</div>
  <div class="topbar"><div class="burger"></div><div class="brand"><span class="brand-dot"></span><span class="brand-name">LINDENHAIN</span></div></div>
  <div class="content">
    <div class="photo jar" role="img" aria-label="Foto Honigglas mit Heidekraut und Honiglöffel"></div>
    <h2>Die gesunden Vorteile von Honig</h2>
    <p class="copy">Lorem ipsum dolor ma sitted amet, consetetur sadipscing elitr, sed diam nonumy eirmod tempor invidunt ut labore et dolore magdena aliquyam erat, sed diam voluptua. At vero eos et accusam et justo duo dolores et ea rebum. Stet clita kasd gubergren, no sea takimata sanctus est Lorem ipsum dolor sit amet. Lorem ipsum dolor sit amet, consetetur sadipscing elitr, sedde diam nonumy eirmod tempored invidunt ut labore et dolore magna aliquyam erat, sed diam voluptua.</p>
    <div class="illus" role="img" aria-label="Illustration Honigwabe"><span></span></div>
  </div>
  <div class="footer">Copyright © 2018 Imkerei Lindenhain | Musterstraße 10 | 12345 Musterstadt | Tel. 012 345 678 | info@lindenhain-imkerei.de | <u>Disclaimer</u> | <u>Impressum</u></div>
</div>

<!-- Grid: Bienenwachs -->
<div class="screen" style="left:345px;top:1431px;width:231px;height:559px">
  <div class="status">iPhone 6/7/8</div>
  <div class="topbar"><div class="burger"></div><div class="brand"><span class="brand-dot"></span><span class="brand-name">LINDENHAIN</span></div></div>
  <div class="content">
    <div class="photo comb" role="img" aria-label="Foto Bienen auf Honigwaben"></div>
    <h2>Das alles kann Bienenwachs</h2>
    <p class="copy">Lorem ipsum dolor ma sitted amet, consetetur sadipscing elitr, sed diam nonumy eirmod tempor invidunt ut labore et dolore magdena aliquyam erat, sed diam voluptua. At vero eos et accusam et justo duo dolores et ea rebum. Stet clita kasd gubergren, no sea takimata sanctus est Lorem ipsum dolor sit amet. Lorem ipsum dolor sit amet, consetetur sadipscing elitr, sedde diam nonumy eirmod tempored invidunt ut labore et dolore magna aliquyam erat, sed diam voluptua.</p>
    <div class="illus" role="img" aria-label="Illustration Bienenwachskerzen, Honig und Kamille"><span></span></div>
  </div>
  <div class="footer">Copyright © 2018 Imkerei Lindenhain | Musterstraße 10 | 12345 Musterstadt | Tel. 012 345 678 | info@lindenhain-imkerei.de | <u>Disclaimer</u> | <u>Impressum</u></div>
</div>

<!-- Grid: Shop -->
<div class="screen" style="left:627px;top:1431px;width:231px;height:866px">
  <div class="status">iPhone 6/7/8</div>
  <div class="topbar"><div class="burger"></div><div class="brand"><span class="brand-dot"></span><span class="brand-name">LINDENHAIN</span></div></div>
  <div class="content">
    <div class="photo jars" role="img" aria-label="Foto drei Honiggläser mit Etikett"></div>
    <h2>Honig aus dem Waldtal</h2>
    <p class="copy">Lorem ipsum dolor ma sitted amet, consetetur sadipscing elitr, sed diam nonumy eirmod tempor invidunt ut labore et dolore magdena aliquyam erat, sed diam voluptua. At vero eos et accusam et justo duo dolores et ea rebum. Stet clita kasd gubergren, no sea takimata sanctus est Lorem ipsum dolor sit amet. Lorem ipsum dolor sit amet, consetetur sadipscing elitr, sedde diam nonumy eirmod tempored invidunt ut labore et dolore magna aliquyam erat, sed diam voluptua.</p>
    <span class="btn">JETZT KAUFEN</span>
    <div class="photo candles" role="img" aria-label="Foto gerollte Kerzen aus Bienenwachs" style="margin-top:38px"></div>
    <h2>Kerzen aus Bienenwachs</h2>
    <p class="copy">Lorem ipsum dolor ma sitted amet, consetetur sadipscing elitr, sed diam nonumy eirmod tempor invidunt ut labore et dolore magdena aliquyam erat, sed diam voluptua. At vero eos et accusam et justo duo dolores et ea rebum. Stet clita kasd gubergren, no sea takimata sanctus est Lorem ipsum dolor sit amet. Lorem ipsum dolor sit amet, consetetur sadipscing elitr, sedde diam nonumy eirmod tempored invidunt ut labore et dolore magna aliquyam erat, sed diam voluptua.</p>
    <span class="btn">JETZT KAUFEN</span>
  </div>
  <div class="footer">Copyright © 2018 Imkerei Lindenhain | Musterstraße 10 | 12345 Musterstadt | Tel. 012 345 678 | info@lindenhain-imkerei.de | <u>Disclaimer</u> | <u>Impressum</u></div>
</div>

<!-- Grid: Kontakt -->
<div class="screen" style="left:907px;top:1431px;width:231px;height:866px">
  <div class="status">iPhone 6/7/8</div>
  <div class="topbar"><div class="burger"></div><div class="brand"><span class="brand-dot"></span><span class="brand-name">LINDENHAIN</span></div></div>
  <div class="content">
    <div class="photo flower" role="img" aria-label="Foto Biene an einer blauen Blüte"></div>
    <h2>Wir freuen uns auf Ihre Nachrichten</h2>
    <div class="form">
      <div class="field">NAME</div>
      <div class="field">EMAIL</div>
      <div class="field area">NACHRICHT</div>
    </div>
    <span class="btn" style="padding:7px 30px">SENDEN</span>
    <div class="biglogo"><span class="mark"></span><span class="name">IMKEREI LINDENHAIN</span></div>
    <div class="illus bee" role="img" aria-label="Illustration fliegende Hummel" style="flex:none;height:90px"><span style="width:80px;height:80px"></span></div>
    <div class="contact">Imkerei Lindenhain<br>Musterstraße 10, 12345 Musterstadt<br>Telefon 012 345 678<br>info@lindenhain-imkerei.de<br><span class="web">www.lindenhain-imkerei.de</span><br><br>Sie finden uns auch auf:</div>
    <div class="social"></div>
  </div>
  <div class="footer">Copyright © 2018 Imkerei Lindenhain | Musterstraße 10 | 12345 Musterstadt | Tel. 012 345 678 | info@lindenhain-imkerei.de | <u>Disclaimer</u> | <u>Impressum</u></div>
</div>

</body>
</html>
```